Double-Gate-Fold Mailer (8-panels)

I have an 8-panel brochure/mailer that I need designed. We're looking for something very classy and professional-looking (both in the fonts and the imagery chosen), as this is for a medical educational event for doctors - and our members are very discerning.

We're open to any design idea that fits within the parameters given below, but if it helps, our primary color is PMS 295 (Hex #002e5a) and we often use PMS 452 (Hex #aaa77e) as a contrasting color.

Images using the NYC skyline or major landmarks are fine, as this will be held in NYC again this year. I have attached photos of the venues that could be used as pop-out images, faded background images or for other inspiration. (I do not have higher-resolution versions of any of the venue photos.)

More info about this event can be found here: http://brelvanguild.org/2017annualmtg/

Important Notes:

- This year's mailer needs to be 20.75" x 8.75” (flat), which will be folded down to 5.19" x 8.75" ultimately.

- I will provide final text for designer, but I have attached last year's mailer so that you can use the content from this as placeholder text. Latin text is also fine - just looking for the design right now.

- *** This year's mailer WILL NOT HAVE a registration form, so please don't include the registration form portion in your design. *** We have, however, added an extra session this year (the day before), so the extra space could be used to promote this new 4-hour event.

- In case it matters to your design, the two events will be in two different locations.

- Final deliverable must include raw files, including main project file (either .ai, .idml, or psd format) and fonts, images, etc.
Updates

Project Deadline Extended Reason: While there are a couple that are interesting and some that are close to our in-house style and tone, I haven't yet seen an outstanding entry (one that followed the directions) yet, especially with respect to subtle/minimal imagery. I would like to give it a few more days. Added Wednesday, July 19, 2017

Target Market(s)

Physicians, nurses, technologists (Please do not use stock images of physicians, nurses, etc. This is a direct-mail brochure; they will know it is for them.)

Industry/Entity Type

Education

Font styles to use
Serif
Sans Serif

Colors

Designer to choose colors to be used in the design.

Requirements
Must have
• Must have room for all content to fit. Last year's brochure is attached as an example of the amount of content there will be. I have attached the five (5) logos that will (eventually) need to be on the brochure. They can be added later either in full color or monotone.
• This year doesn't have a theme like last year. The title of the event is simply: "The 89th Annual Scientific Session & Inaugural PQR Quillbox Challenge"
Nice to have
• Nice to have a design that somehow coordinates with our logos, which, as you can see, range in color from dark blue to light blue, but this isn't necessary, as our logos can all be monotone if necessary. It would be nice if the designer could keep the horizontal-style of the art, similar to last year's, but it's not a requirement.
Should not have
• Images should be subtle, faded or pushed to the background. Please don't include stock images of people, physicians working, medical equipment, etc. (This is a highly specialized field of medicine, and generic stock images look very strange and, at best, are a misrepresentation of these doctors.) Art should not be to "cartoon-y" either or have too many distracting images.

```html
<!DOCTYPE html>
<html lang="en">
<head>
<meta charset="utf-8">
<title>Brelvan Cardiological Guild – 89th Annual Scientific Session Mailer</title>
<link rel="stylesheet" href="https://fonts.googleapis.com/css2?family=Ubuntu:wght@400;500;700&family=Open+Sans:ital,wght@0,300;0,400;0,600;0,700;1,400&display=swap">
<style>
:root{
  --navy:#1d2b55;
  --tan:#aaa77e;
  --tan-light:#d8d5bc;
  --tan-panel:#cdcaae;
  --paper:#ffffff;
  --bg:#eceae6;
  --ink:#1d2b55;
  --muted:#4a5577;
}
*{box-sizing:border-box;margin:0;padding:0}
html,body{width:1200px;height:1200px;overflow:hidden;background:var(--bg)}
body{position:relative;font-family:"Open Sans",Arial,sans-serif;color:var(--ink)}

.spread{position:absolute;left:51px;width:1098px;height:464px;overflow:hidden;box-shadow:0 2px 6px rgba(0,0,0,.18)}
.spread--outside{top:112px;background:var(--paper)}
.spread--inside{top:624px;background:var(--navy)}

.panel{position:absolute;top:0;height:100%;overflow:hidden}

/* ---------- outside: governance panel ---------- */
.panel--boards{left:0;width:274px;padding:12px 10px 0 11px}
.org{padding-bottom:8px}
.org + .org{border-top:1.5px dotted var(--tan);padding-top:8px}
.org__title{font-size:8.6px;font-weight:700;margin-bottom:6px}
.org__cols{display:flex;gap:6px}
.org__col{width:90px}
.org__col--wide{width:150px}
.org__head{font-size:6.4px;font-weight:700;text-transform:uppercase;margin-bottom:1px}
.org__list{list-style:none;font-size:5.2px;line-height:1.28}
.org__list em{font-style:italic;color:var(--muted)}
.org__list .role{display:block;font-style:italic;margin-bottom:1.5px}

/* ---------- outside: mailing panel ---------- */
.panel--mailer{left:274px;width:275px}
.return-address,.mail-note{position:absolute;transform:rotate(-90deg);transform-origin:left top;font-size:6.6px;line-height:1.3;white-space:nowrap}
.return-address{left:121px;top:374px}
.mail-note{left:276px;top:424px}
.seal{position:absolute;left:118px;top:394px;width:40px;height:40px;border-radius:50%;border:1.5px solid var(--navy)}

/* ---------- outside: cover ---------- */
.panel--cover{left:549px;width:275px;color:var(--paper)}
.cover__art{position:absolute;inset:0;background:linear-gradient(180deg,#efece2 0%,#dedacb 22%,#b7b39a 42%,#52608a 62%,var(--navy) 78%,var(--navy) 100%)}
.cover__brand{position:absolute;left:27px;top:14px;display:flex;align-items:center;gap:8px;color:var(--navy);font-size:11px}
.cover__brand .dot{width:30px;height:30px;border-radius:50%;background:var(--navy)}
.cover__title{position:absolute;left:27px;top:64px;width:250px;font-family:"Ubuntu",sans-serif;font-weight:700;color:var(--navy);font-size:21.5px;line-height:1.16}
.cover__title .light{font-weight:300}
.cover__dates{position:absolute;left:27px;top:212px;font-family:"Ubuntu",sans-serif;font-weight:500;font-size:12.4px;line-height:1.08}
.cover__dates .day{color:var(--tan-light);opacity:.9}
.cover__dates .strong{color:var(--paper)}
.cover__dates p + p{margin-top:10px}
.partners{position:absolute;left:27px;top:322px;width:240px}
.partner{display:flex;align-items:center;gap:6px;font-size:5.6px;line-height:1.25;color:var(--paper);margin-bottom:9px;width:120px}
.partner .mark{flex:none;width:26px;height:26px;border-radius:50%;border:1.3px solid var(--paper)}
.partner--side{position:absolute;left:106px;top:93px}

/* ---------- outside: program ---------- */
.panel--program{left:824px;width:274px;padding:18px 14px 0 14px}
.program h2{font-size:8.8px;font-weight:700;text-transform:uppercase;margin-bottom:2px}
.program p{font-size:5.6px;line-height:1.2;margin-bottom:3px}
.program h2:not(:first-child){margin-top:3px}
.program ul{list-style:none;font-size:5.6px;line-height:1.2}
.program li{padding-left:5px;text-indent:-5px;margin-bottom:2.6px}
.program li::before{content:"• "}

/* ---------- inside ---------- */
.map-art{position:absolute;left:0;top:230px;width:293px;height:234px;background:linear-gradient(160deg,#6d7698 0%,#c9cad6 40%,#a8adc2 70%,#7c84a4 100%)}
.reception{position:absolute;left:21px;top:21px;width:230px;height:224px;background:var(--paper);padding:8px}
.reception__frame{border:1.5px solid var(--tan);height:100%;padding:9px 8px 0 12px}
.reception__title{font-family:"Ubuntu",sans-serif;font-weight:700;font-size:20.5px;line-height:1.22;margin-bottom:6px}
.reception__meta{font-weight:300;font-size:13.6px;line-height:1.1;margin-bottom:8px}
.reception__meta p + p{margin-top:6px}
.reception__times{display:grid;grid-template-columns:78px 1fr;font-size:10.4px;row-gap:3px;line-height:1.15}

.details{position:absolute;left:293px;top:21px;width:664px;height:421px;background:var(--paper);padding:10px}
.details__frame{position:relative;border:1.5px solid var(--tan);height:100%}
.logistics{position:absolute;left:9px;top:8px;width:120px}
.logistics h3{font-family:"Ubuntu",sans-serif;font-weight:500;color:var(--tan);font-size:11.5px;margin-bottom:3px}
.logistics h3:not(:first-child){margin-top:8px}
.logistics p{font-size:5.3px;line-height:1.22;margin-bottom:3px}
.logistics b{font-weight:700}
.divider{position:absolute;left:136px;top:8px;bottom:8px;border-left:1.3px dotted var(--tan)}

.agenda{position:absolute;left:142px;top:4px;right:8px;bottom:6px;display:flex;flex-direction:column}
.agenda__head{display:flex;align-items:baseline;justify-content:space-between;white-space:nowrap}
.agenda h2{font-family:"Ubuntu",sans-serif;font-weight:700;font-size:24px;line-height:1.3;white-space:nowrap}
.agenda__date{font-weight:300;font-size:12.6px}
.agenda__sub{font-weight:300;font-size:13.6px;line-height:1.2;margin-bottom:8px;white-space:nowrap}
.heart-art{position:absolute;right:0;top:60px;width:66px;height:100px;background:radial-gradient(ellipse at center,rgba(170,167,126,.28),rgba(170,167,126,0) 70%)}
.agenda__body{display:grid;grid-template-columns:300px 1fr;column-gap:12px;position:relative}
.schedule{font-size:6.8px;line-height:1.18}
.schedule__row{display:grid;grid-template-columns:40px 1fr;margin-bottom:2.8px}
.faculty{font-size:5.9px;line-height:1.18}
.faculty h4{font-size:8px;font-weight:700;text-transform:uppercase;margin-bottom:1px}
.faculty h4:not(:first-child){margin-top:5px}
.faculty .person{margin-bottom:2.5px}
.faculty .name{font-weight:700;text-transform:uppercase}
.faculty em{font-style:italic;display:block}
.faculty .thanks{font-size:5.3px;margin-top:7px;line-height:1.22}

.info-rail{position:absolute;right:0;top:0;width:121px;height:100%;background:var(--tan-panel);padding:10px 9px 0 13px}
.info-rail h5{font-size:7.2px;font-weight:700;margin-bottom:1px}
.info-rail h5:not(:first-child){margin-top:5px}
.info-rail p{font-size:5.3px;line-height:1.24}
</style>
</head>
<body>

<!-- Outside spread -->
<section class="spread spread--outside">

  <div class="panel panel--boards">
    <div class="org">
      <h2 class="org__title">The Brelvan Cardiological Guild, Inc.</h2>
      <div class="org__cols">
        <div class="org__col">
          <h3 class="org__head">Officers</h3>
          <ul class="org__list">
            <li>Owen R. Castell, MD, FACC<span class="role">President</span></li>
            <li>Arthur Penrose, MD, FACC<span class="role">Immediate Past President</span></li>
            <li>Rafael Ostrand, MD, FACC<span class="role">Secretary-Treasurer</span></li>
            <li>Elena Marsh, MA, MSA<span class="role">Executive Director</span></li>
          </ul>
        </div>
        <div class="org__col org__col--wide">
          <h3 class="org__head">Executive Board</h3>
          <ul class="org__list">
            <li>Carl Abernathy, MD, PhD</li><li>Gavin T. Brisk, MD</li><li>Lin Haoran, MD, MPH</li>
            <li>Peter D. Calloway, MD</li><li>Paul Renner, MD</li><li>Ilana Vesk, MD</li>
            <li>Joseph Merriam, MD</li><li>Arthur Penrose, MD</li><li>Owen R. Castell, MD</li>
            <li>James K. Orlo, MD</li><li>Harold B. Tenney Jr., MD</li><li>Victor Ashlund, MD</li>
            <li>Andrew Van Dell, MD</li><li>Daniel P. Wexley, MD</li><li>Samir Haddan, MD</li>
          </ul>
        </div>
      </div>
    </div>

    <div class="org">
      <h2 class="org__title">Harborview Cardiac Center</h2>
      <div class="org__cols">
        <div class="org__col">
          <h3 class="org__head">Officers</h3>
          <ul class="org__list">
            <li>Richard M. Hollin<span class="role">President</span></li>
            <li>Martin L. Wyeth, MD<span class="role">Executive Vice President</span></li>
            <li>David S. Fenwick<span class="role">Secretary</span></li>
            <li>Alfred T. Greer<span class="role">Treasurer</span></li>
          </ul>
        </div>
        <div class="org__col org__col--wide">
          <h3 class="org__head">Board of Governors</h3>
          <ul class="org__list">
            <li>Michael Dorne, DDS</li><li>Edward Lusk</li><li>David S. Fenwick</li>
            <li>Hon. Bertram Hale</li><li>David Hollin, Esq.</li><li>Richard M. Hollin</li>
            <li>Alfred T. Greer</li><li>Jerome Pratt</li><li>Eric Sandoval, Esq.</li>
            <li>Jeffrey Auden</li><li>Michael Tarrant, DDS</li><li>Lisa Coyle, MD</li>
            <li>Martin L. Wyeth, MD</li><li>Robert Wyeth</li>
          </ul>
        </div>
      </div>
    </div>

    <div class="org">
      <h2 class="org__title">Brelvan State Chapter, Allied College of Cardiology</h2>
      <div class="org__cols">
        <div class="org__col">
          <h3 class="org__head">Officers</h3>
          <ul class="org__list">
            <li>Arthur Penrose, MD, FACC<span class="role">President</span></li>
            <li>Owen R. Castell, MD, FACC<span class="role">Immediate Past President</span></li>
            <li>Rafael Ostrand, MD, FACC<span class="role">Secretary-Treasurer</span></li>
            <li>Elena Marsh, MA, MSA<span class="role">Executive Director</span></li>
          </ul>
        </div>
        <div class="org__col org__col--wide">
          <h3 class="org__head">Councilors</h3>
          <ul class="org__list">
            <li>Richard Avalon, MD, <em>New Rochelle</em></li><li>Jay R. Belcourt, MD, <em>Manhasset</em></li>
            <li>Dmitri A. Varga, MD, <em>Manhattan</em></li><li>Stanley P. Ocampo, MD, <em>Buffalo</em></li>
            <li>Ken Ishara, MD, <em>Valhalla</em></li><li>Norma J. Whitlock, MD, <em>Manhattan</em></li>
            <li>Lloyd E. Marten, MD, <em>Stony Brook</em></li><li>Charles W. Linden, MD, <em>Rochester</em></li>
            <li>Amir N. Soliman, MD, <em>East Meadow</em></li><li>Arun V. Desai, MD, <em>Utica</em></li>
            <li>Robert C. Lam, MD, <em>Albany</em></li><li>Brian K. Stahl, MD, <em>Buffalo</em></li>
            <li>Michael F. Ostler, MD, <em>Utica</em></li><li>Benjamin L. Kroft, MD, <em>Rhinebeck</em></li>
            <li>Manpreet K. Gill, MD, Albany</li><li>John Reid Tolliver, MD, <em>Rochester</em></li>
            <li>Theodore J. Brandt, MD, <em>Manhattan</em></li>
          </ul>
        </div>
      </div>
    </div>
  </div>

  <div class="panel panel--mailer">
    <p class="return-address">The Brelvan Cardiological Guild, Inc.<br>410 Larkmoor Avenue, Suite 1200<br>Fairhaven, NY 10920</p>
    <div class="seal" aria-hidden="true"></div>
    <p class="mail-note">• 89th Annual Scientific Session<br>&nbsp;&nbsp;The Brelvan Cardiological Guild, Inc.<br>• 27th Annual Meeting,<br>&nbsp;&nbsp;Brelvan State Chapter,<br>&nbsp;&nbsp;Allied College of Cardiology</p>
  </div>

  <div class="panel panel--cover">
    <div class="cover__art" role="img" aria-label="Faded city skyline fading into a navy field with a fine-line engraved heart"></div>
    <div class="cover__brand"><span class="dot"></span><span>Brelvan State Chapter</span></div>
    <h1 class="cover__title">The 89<sup style="font-size:.55em">th</sup> Annual Scientific Session<br><span class="light">&amp;</span><br><span class="light">Inaugural</span> PQR Quillbox Challenge</h1>
    <div class="cover__dates">
      <p class="day">Wednesday<br>December 6th 2017<br>6:30pm - 10:30pm</p>
      <p class="strong">Thursday<br>December 7th 2017<br>7:30am - 3:30pm</p>
    </div>
    <div class="partners">
      <div class="partner"><span class="mark"></span><span>Brelvan<br>Cardiological<br>Guild Inc.</span></div>
      <div class="partner"><span class="mark"></span><span>In association<br>with Harborview<br>Cardiac Center</span></div>
      <div class="partner"><span class="mark"></span><span>Veldran<br>Institute for<br>Medicine</span></div>
      <div class="partner partner--side"><span class="mark"></span><span>Northbay Chapter<br>Exchange Program</span></div>
    </div>
  </div>

  <div class="panel panel--program program">
    <h2>Program Description</h2>
    <p>This annual event brings together cardiologists, cardio-thoracic surgeons, internists, family practitioners, gerontologists, oncologists, cardiac nurse practitioners, physician assistants, cardiology fellows in training (FITs) and all members of the cardiac care team. The event is presented by the Brelvan Cardiological Guild, the Brelvan State Chapter of the Allied College of Cardiology and Harborview Cardiac Center.</p>
    <p>The Annual Scientific Session also features the winners of the Annual Young Investigators' Competition, which is now open, and this year will ALSO feature the winners of the Inaugural PQR Quillbox Challenge!</p>
    <h2>Target Audience</h2>
    <p>The target audience includes cardiologists, cardiothoracic surgeons, internists, family medicine practitioners, gerontologists, oncologists, cardiac nurse practitioners, physician assistants, cardiology fellows-in-training and all members of the cardiac care team.</p>
    <h2>Program Objectives</h2>
    <p>At the completion of this program, physicians and other healthcare professionals in attendance will be able to:</p>
    <ul>
      <li>Explain the rationale for, and identify components of, a comprehensive approach to readmission reduction</li>
      <li>Describe the importance of high-quality, disease-specific care, multiple transitional care interventions, involvement of multidisciplinary teams, and early and frequent outpatient followup</li>
      <li>Navigate the current landscapes of Post-Acute Care and describe its relevance in the care of our geriatric cardiology patients</li>
      <li>Identify gaps in care and specific interventions providers can utilize to improve outcomes</li>
      <li>Identify various types of procedures necessary for treating atrial fibrillation in older adults</li>
      <li>Explain the rationale for why the management of atrial fibrillation is directed at preventing thromboembolism and controlling heart rate and rhythm</li>
      <li>Identify the effects of aging on CV care and unique aspects of care for older adults</li>
      <li>Delineate the various phenotypes of aortic stenosis in older adults and enumerate mechanisms underlying paradoxically low-flow aortic stenosis</li>
      <li>Identify TTR cardiac amyloid without a biopsy</li>
      <li>Explain the extent to which current guidelines for cardiovascular disorders are evidence-based with respect to older adults</li>
      <li>Identify strategies for improving care and outcomes for older adults with cardiovascular diseases</li>
      <li>Describe the role of non-invasive imaging for diagnosis of cardiac amyloids</li>
      <li>Recite promising treatments for TTR cardiac amyloidosis</li>
      <li>Describe ways in which telemonitoring can improve heart failure outcomes</li>
      <li>Describe patients' perspectives about the pros and cons of telemonitoring</li>
      <li>Identify management strategies in diagnosing acute MI in elderly patients</li>
    </ul>
  </div>
</section>

<!-- Inside spread -->
<section class="spread spread--inside">
  <div class="map-art" role="img" aria-label="Street map of the city around the two event venues"></div>

  <div class="reception">
    <div class="reception__frame">
      <h2 class="reception__title">PQR Quillbox<br>Cocktail Reception<br>Whiskey Tasting</h2>
      <div class="reception__meta">
        <p>6 December 2017</p>
        <p>Oak &amp; Ember, 14 Harlow St,<br>Fairhaven, NY 10921</p>
      </div>
      <div class="reception__times">
        <span>6:30-10:30pm</span><span>Cocktail Reception &amp;<br>Whiskey Tasting</span>
        <span>8:30-9:30pm</span><span>PQR Quillbox<br>Challenge</span>
      </div>
    </div>
  </div>

  <div class="details">
    <div class="details__frame">
      <div class="logistics">
        <h3>When</h3>
        <p><b>Cocktail Reception, Whiskey Tasting &amp; Inaugural PQR Quillbox Challenge:</b></p>
        <p>Wednesday, Dec. 6th, 2017, from 6:30 to 10:30 p.m. | Click here for more info.</p>
        <p><b>Scientific Session:</b></p>
        <p>Thursday, Dec. 7th, 2017, from 7:30 a.m. to 3 p.m.</p>
        <h3>Where</h3>
        <p><b>Cocktail Reception, Whiskey Tasting &amp; Inaugural PQR Quillbox Challenge:</b></p>
        <p>Oak &amp; Ember, 14 Harlow St, Fairhaven, NY 10921</p>
        <p><b>Scientific Session:</b></p>
        <p>The Wrenfield Ballroom, 22 Calder St, Fairhaven, NY 10921</p>
        <h3>Accommodation</h3>
        <p><b>Should you want a hotel closer to the event (the educational session), there is courtesy room block at:</b></p>
        <p>The Aldine at Kestrel Park (10-minute walk from the Wrenfield Ballroom)</p>
        <p>Should you want a hotel closer to Oak &amp; Ember, where the prior night's Cocktail Reception &amp; Quillbox Challenge will be held, there are courtesy room blocks at:</p>
        <p>The Halvern (4-min. walk to Oak &amp; Ember) | Call 800-555-0142 and mention "Brelvan Cardiological Guild" for a rate of $309 (excl. taxes) for a room with a king-size bed</p>
        <p>[Offer expires 11/08/17]</p>
        <p>The Merrow (7-min. walk to Oak &amp; Ember) | Call 888-555-0178 and mention "Brelvan Cardiological Guild" for a rate of $259 (excl. taxes) for a room with a king-size bed</p>
        <p>[Offer expires 11/07/17]</p>
      </div>
      <div class="divider"></div>

      <div class="agenda">
        <div class="heart-art" role="img" aria-label="Faint fine-line engraved heart"></div>
        <div class="agenda__head"><h2>PQR Quillbox</h2><span class="agenda__date">Wednesday, December 6th 2017 ~ 6:30-10:30pm</span></div>
        <h2>89th Annual Scientific Session</h2>
        <p class="agenda__sub">Thursday, December 7th 2017 ~ 7:30am-3pm</p>

        <div class="agenda__body">
          <div class="schedule">
            <div class="schedule__row"><span>7:30 a.m.</span><span>Registration, Posters, Exhibits &amp; Continental Breakfast</span></div>
            <div class="schedule__row"><span>8:10 a.m.</span><span>Opening Remarks and Business Meeting<br>Owen Castell, MD, FACC; Arthur Penrose, MD, FACC; Jonah Pickett, MD, FACC; Matthias Reinholt, MD, FACC</span></div>
            <div class="schedule__row"><span>8:30 a.m.</span><span>Strategies to Reduce Cardiovascular Readmissions in Older Patients<br>Vikram Raghunath, MD, MBA</span></div>
            <div class="schedule__row"><span>9:00 a.m.</span><span>Post-Acute Care for Older Adults with CVD - What Do We Need to Know?<br>Nadia Ellery, MD, FACC</span></div>
            <div class="schedule__row"><span>9:30 a.m.</span><span>Afib in Older Adults: Warfarin, NOACS, LAA Occlusion, Bleeding<br>Jonah Pickett, MD, FACC</span></div>
            <div class="schedule__row"><span>10:00 a.m.</span><span>Paradoxically Low Flow Aortic Stenosis: An Emerging Complex Phenotype in Older Adults<br>Matthias Reinholt, MD, FACC</span></div>
            <div class="schedule__row"><span>10:30 a.m.</span><span>Refreshment Break, Posters, Exhibits</span></div>
            <div class="schedule__row"><span>10:45 a.m.</span><span>The Harborview Cardiac Center Lecture: Gaps in the Guidelines for Older Adults with Cardiovascular Disease<br>Miles Fairburn, MD, FACC</span></div>
            <div class="schedule__row"><span>11:15 a.m.</span><span>Case Presentations</span></div>
            <div class="schedule__row"><span>12:30 p.m.</span><span>Luncheon Symposium: PYP Scanning for Diagnosing TTR Amyloid without a Biopsy: Re-Emergence of Nuclear Cardiology<br>Samira Kazmi, MD, FACC</span></div>
            <div class="schedule__row"><span>1:15 p.m.</span><span>Posters, Exhibits &amp; Review of Morning Talks</span></div>
            <div class="schedule__row"><span>1:30 p.m.</span><span>The Hollis-Varnet Lecture: Telemedicine in Older Adults with Heart Failure: High Tech But Not High Touch<br>Sana Qureshi, MD</span></div>
            <div class="schedule__row"><span>2:00 p.m.</span><span>The Castell-Brandt Lecture: Treating MI in Older Adults: What's Different?<br>Joel Arkwright, MD, FACC</span></div>
            <div class="schedule__row"><span>2:30 p.m.</span><span>Discussion, Review of Presentations &amp; Closing Remarks</span></div>
            <div class="schedule__row"><span>3:00 p.m.</span><span>Scientific Session Ends</span></div>
          </div>

          <div class="faculty">
            <h4>Faculty</h4>
            <div class="person"><span class="name">Vikram Raghunath, MD, MBA</span><em>Assistant Professor of Medicine</em>Ashgrove University School of Medicine</div>
            <div class="person"><span class="name">Nadia Ellery, MD, FACC</span><em>Assistant Professor</em>Penwick University School of Medicine</div>
            <div class="person"><span class="name">Jonah Pickett, MD, FACC</span><em>Assistant Professor of Medicine and Population Health Director, Geriatric Cardiology Program</em>Kestrel University Medical Center</div>
            <div class="person"><span class="name">Matthias Reinholt, MD, FACC</span><em>Elias and Mara Quint Professor of Medicine</em>Halloway University Medical Center</div>
            <div class="person"><span class="name">Miles Fairburn, MD, FACC</span><em>Professor of Medicine</em>Merrifield University School of Medicine</div>
            <div class="person"><span class="name">Samira Kazmi, MD, FACC</span><em>Associate Professor of Medicine-Cardiology</em>Halloway University Medical Center</div>
            <div class="person"><span class="name">Sana Qureshi, MD</span><em>Associate Professor</em>Ashgrove University School of Medicine, Dept. of General Internal Medicine</div>
            <div class="person"><span class="name">Joel Arkwright, MD, FACC</span><em>Professor of Medicine and Editor in Chief, The Meridian Journal of Medicine</em>Sandvale University College of Medicine</div>
            <h4>Planning Committee</h4>
            <div>Lin Haoran, MD, MPH<br>Jonah Pickett, MD<br>Arthur Penrose, MD<br>Owen R. Castell, MD<br>Matthias Reinholt, MD</div>
            <p class="thanks">The Brelvan Cardiological Guild and the Brelvan State Chapter of the Allied College of Cardiology thank Harborview Cardiac Center for its continuing educational support.</p>
          </div>
        </div>
      </div>
    </div>
  </div>

  <aside class="info-rail">
    <h5>General Information</h5>
    <p>This conference is presented by the Brelvan Cardiological Guild, Inc. of the Brelvan State Chapter, Allied College of Cardiology, in association with Harborview Cardiac Center and jointly provided by the Calder School of Medicine and Dentistry.</p>
    <h5>Accreditation</h5>
    <p>This activity has been planned and implemented in accordance with the accreditation requirements and policies of the Continuing Education Accreditation Board (CEAB) through the joint providership of the Calder School of Medicine and Dentistry and the Brelvan Cardiological Guild, Inc. The Calder School of Medicine and Dentistry is accredited by the CEAB to provide continuing medical education for physicians.</p>
    <h5>Certification</h5>
    <p>The Calder School of Medicine and Dentistry designates this live activity for a maximum of 6.25 CEAB Category 1 Credits. Physicians should claim only the credit commensurate with the extent of their participation in the activity.</p>
    <h5>Disclosure Statement</h5>
    <p>The Brelvan Cardiological Guild, Inc. relies upon invited faculty participants in its CME programs to provide educational information that is objective and free of bias. In this spirit, and in accordance with the guidelines of the program sponsor, faculty participants are expected to indicate any commercial relationship that might be perceived as a real or apparent conflict of interest. Any discussion of investigational or unlabeled uses of a product will be identified.</p>
    <h5>Hotel Information</h5>
    <p>A courtesy hotel block at the Hotel Event has been reserved for this event. To get the discounted rate, call (866) 555-0119 to reserve your room night(s) and use the reference code "Cardiology for the Ages."</p>
    <h5>Additional Information</h5>
    <p>Email ask@brelvanguild.org or<br>(212) 555-0164</p>
  </aside>
</section>

</body>
</html>
```